I will ask the design of the business card

We are looking for business card design of the new company "TORVIK QUANTA WORKS LLC." Based in Azerbaijan.
In case
We are working on Azerbaijan to set up the first exchange of crypto currencies.

The key currency used in exchanges is called "MELDA".
In case
We are doing project to make crypto currency infrastructure.

We provide state-of-the-art technology to the world.

```html
<!DOCTYPE html>
<html lang="en">
<head>
<meta charset="utf-8">
<title>Torvik Quanta Works LLC. — Business Card</title>
<link rel="stylesheet" href="https://fonts.googleapis.com/css2?family=Cinzel:wght@500&family=Open+Sans:wght@400&display=swap">
<style>
  :root {
    --brand-red: #a01a1c;
    --paper: #ffffff;
    --ink: #2b2b2b;
    --rule: #b5b5b5;
    --backdrop: #e9e9e9;
    --shadow: rgba(0, 0, 0, 0.18);
  }
  * { margin: 0; padding: 0; box-sizing: border-box; }
  html, body {
    width: 1200px; height: 782px; overflow: hidden;
    background: var(--backdrop);
  }
  .stage {
    position: relative; width: 1200px; height: 782px;
  }
  .card {
    position: absolute; width: 540px; height: 309px;
    box-shadow: 0 6px 18px var(--shadow);
  }
  .card--back {
    left: 630px; top: 236px;
    background: var(--brand-red);
    display: flex; align-items: center; justify-content: center;
  }
  .card--front {
    left: 30px; top: 236px;
    background: var(--paper);
  }
  .wordmark {
    font-family: "Cinzel", serif; font-weight: 500;
    text-align: center; line-height: 1.15; letter-spacing: 1px;
  }
  .card--back .wordmark { color: var(--paper); font-size: 34px; }
  .card--front .wordmark {
    position: absolute; left: 250px; top: 86px; width: 270px;
    color: var(--brand-red); font-size: 27px;
  }
  .holder {
    position: absolute; left: 30px; top: 34px;
  }
  .holder__name {
    font-family: "Cinzel", serif; font-weight: 500;
    color: var(--brand-red); font-size: 17px; letter-spacing: 0.5px;
  }
  .holder__role {
    font-family: "Open Sans", sans-serif; font-size: 11.5px; color: var(--ink);
    margin-top: 1px;
  }
  .contacts {
    list-style: none; margin-top: 12px;
    font-family: "Open Sans", sans-serif; font-size: 13px; color: var(--ink);
  }
  .contacts li { display: flex; align-items: center; gap: 6px; height: 19px; }
  .contacts svg { width: 11px; height: 11px; fill: var(--brand-red); flex: none; }
  .divider {
    position: absolute; left: 30px; right: 30px; top: 205px;
    border-top: 1px solid var(--rule);
  }
  .address {
    position: absolute; right: 40px; top: 222px; text-align: left;
    font-family: "Open Sans", sans-serif; font-size: 13.5px; color: var(--ink);
    line-height: 1.4;
  }
</style>
</head>
<body>
<main class="stage">
  <section class="card card--front">
    <div class="holder">
      <p class="holder__name">Elnar Rustamov</p>
      <p class="holder__role">Managing Director</p>
      <ul class="contacts">
        <li><svg viewBox="0 0 12 12"><path d="M2 1h2.5l1 3-1.5 1a7 7 0 0 0 3 3l1-1.5 3 1V10a1 1 0 0 1-1 1A10 10 0 0 1 1 2a1 1 0 0 1 1-1z"/></svg>012-555 0148</li>
        <li><svg viewBox="0 0 12 12"><path d="M3.5 0h5a1 1 0 0 1 1 1v10a1 1 0 0 1-1 1h-5a1 1 0 0 1-1-1V1a1 1 0 0 1 1-1zM4 1.5v7.5h4V1.5z"/></svg>012-555 0149</li>
        <li><svg viewBox="0 0 12 12"><path d="M0 2h12v8H0zM1 3l5 4 5-4v-.2H1z"/></svg>info@torvikquanta.az</li>
        <li><svg viewBox="0 0 12 12"><circle cx="6" cy="6" r="6"/></svg>www.torvikquanta.az</li>
      </ul>
    </div>
    <h2 class="wordmark">Torvik Quanta<br>Works LLC.</h2>
    <hr class="divider">
    <address class="address" style="font-style:normal">
      27 Nizami Street, Baku<br>Azerbaijan, AZ1000
    </address>
  </section>

  <section class="card card--back">
    <h1 class="wordmark">Torvik Quanta<br>Works LLC.</h1>
  </section>
</main>
</body>
</html>
```